corvane business cards

Hey design gurus!
I'm after a clean, modern, stylish business card for my about to be launched company.
I've uploaded the logos for my company "Corvane Electrical Solutions"
and also the brightway electricians logo to whom i am associated.

```html
<!DOCTYPE html>
<html lang="en">
<head>
<meta charset="utf-8">
<title>Corvane Electrical Solutions – Business Cards</title>
<link rel="stylesheet" href="https://fonts.googleapis.com/css2?family=Montserrat:wght@500;600;700;800&display=swap">
<style>
  :root{
    --page:#e6e7e9;
    --navy:#0f1a2a;
    --navy-deep:#0a1220;
    --blue:#1f86d6;
    --white:#ffffff;
    --silver-1:#2a3340;
    --silver-2:#c9ced6;
    --ink-soft:#c8d3e0;
  }
  *{margin:0;padding:0;box-sizing:border-box}
  html,body{width:1200px;height:2656px;overflow:hidden;background:var(--page);font-family:"Montserrat",sans-serif}
  .sheet{position:relative;width:1200px;height:2656px}
  .card{position:absolute;left:112px;width:976px;height:552px;overflow:hidden;box-shadow:0 6px 18px rgba(0,0,0,.18)}
  .card--front{top:752px;background:radial-gradient(ellipse at 70% 40%,#16243a 0%,var(--navy) 55%,var(--navy-deep) 100%)}
  .card--back{top:1352px;background:var(--white)}

  /* brand lockup */
  .brand{position:absolute;display:flex;align-items:center;gap:26px}
  .brand__dot{width:104px;height:104px;border-radius:50%;background:var(--blue);flex:none}
  .brand__name{color:var(--blue);font-weight:800;line-height:1}
  .brand__name span{display:block}
  .brand__word{font-size:74px;letter-spacing:3px}
  .brand__sub{font-size:21px;letter-spacing:5.2px;margin-top:8px}
  .card--front .brand{left:150px;top:150px}

  .web-band{position:absolute;left:0;right:0;top:272px;height:80px;
    background:linear-gradient(90deg,rgba(42,51,64,0) 0%,var(--silver-1) 25%,var(--silver-2) 60%,var(--silver-1) 90%,rgba(42,51,64,0) 100%)}
  .web{position:absolute;left:0;right:0;top:290px;text-align:center;color:var(--white);font-size:34px;font-weight:600;letter-spacing:2px}
  .web b{color:var(--blue);font-weight:800}

  /* back */
  .card--back .brand{left:40px;top:40px}
  .card--back .brand__word{font-size:60px;letter-spacing:2px}
  .card--back .brand__sub{font-size:17px;letter-spacing:4.4px}
  .info-band{position:absolute;left:0;top:160px;width:800px;height:320px;background:var(--navy);
    clip-path:polygon(0 0,100% 0,88% 100%,0 100%)}
  .person{position:absolute;left:40px;top:180px;color:var(--white)}
  .person__name{font-size:44px;font-weight:800;letter-spacing:1.5px}
  .person__role{font-size:18px;font-weight:600;letter-spacing:7px;color:var(--ink-soft);margin-top:6px}
  .contacts{position:absolute;left:40px;top:272px;list-style:none;color:var(--white);font-size:23px;font-weight:500}
  .contacts li{display:flex;align-items:flex-start;gap:16px;margin-bottom:18px;line-height:1.3}
  .contacts svg{flex:none;width:32px;height:32px}
  .emblem{position:absolute;left:688px;top:172px;width:280px;height:280px;border-radius:50%;background:var(--blue);border:14px solid var(--white)}
  .partner-badge{position:absolute;left:40px;top:496px;width:104px;height:40px;background:var(--navy);border-left:8px solid #b04040}
</style>
</head>
<body>
<main class="sheet">

  <section class="card card--front" aria-label="Business card front">
    <div class="brand">
      <div class="brand__dot"></div>
      <p class="brand__name"><span class="brand__word">CORVANE</span><span class="brand__sub">ELECTRICAL SOLUTIONS</span></p>
    </div>
    <div class="web-band"></div>
    <p class="web">www.<b>corvane</b>.com</p>
  </section>

  <section class="card card--back" aria-label="Business card back">
    <div class="brand">
      <p class="brand__name"><span class="brand__word">CORVANE</span><span class="brand__sub">ELECTRICAL SOLUTIONS</span></p>
    </div>
    <div class="info-band"></div>
    <div class="person">
      <h1 class="person__name">MARCUS T. HALE</h1>
      <p class="person__role">OWNER</p>
    </div>
    <ul class="contacts">
      <li>
        <svg viewBox="0 0 32 32"><circle cx="16" cy="16" r="16" fill="#1f86d6"/><path d="M11 8.5l3 3-2 2.2c1 2.2 2.8 4 5 5l2.2-2 3 3-2.3 2.6c-5.5-.6-10.4-5.5-11-11z" fill="#fff"/></svg>
        +234 5550 1842
      </li>
      <li>
        <svg viewBox="0 0 32 32"><circle cx="16" cy="16" r="16" fill="#1f86d6"/><rect x="8" y="10.5" width="16" height="11" rx="1.5" fill="#fff"/><path d="M8.5 11.5l7.5 6 7.5-6" fill="none" stroke="#1f86d6" stroke-width="1.6"/></svg>
        info@corvane.com
      </li>
      <li>
        <svg viewBox="0 0 32 32"><circle cx="16" cy="16" r="16" fill="#1f86d6"/><path d="M16 7a6 6 0 0 0-6 6c0 4.5 6 12 6 12s6-7.5 6-12a6 6 0 0 0-6-6z" fill="#fff"/><circle cx="16" cy="13" r="2.2" fill="#1f86d6"/></svg>
        <span>48B Street 3 Harbor Road,<br>Las Vegas</span>
      </li>
    </ul>
    <div class="emblem"></div>
    <div class="partner-badge" aria-label="Brightway Electricians partner badge"></div>
  </section>

</main>
</body>
</html>
```